menu board design: harbor burger

we are a burger restaurant.
we need to re design our menu board to fit within the new design of the restaurant. we are after something simple and easy to read. the overall look and feel of the design should be inline with the design of the shop.

Target Market(s)

18-40 male and female

Colors

Designer to choose colors to be used in the design.

Requirements
Must have
• easy to read. good layout. white background. branding included in design.

```html
<!DOCTYPE html>
<html lang="en">
<head>
<meta charset="utf-8">
<title>Harbor Burger – Menu Board</title>
<link href="https://fonts.googleapis.com/css2?family=Oswald:wght@400;500;600;700&family=Josefin+Sans:wght@600&display=swap" rel="stylesheet">
<style>
  :root {
    --page: #cfcfcf;
    --brick: #a51c22;
    --brick-dark: #3a1d18;
    --panel: #ffffff;
    --blue: #1f4fa3;
    --ink: #1a1a1a;
  }
  * { box-sizing: border-box; margin: 0; padding: 0; }
  html, body { width: 1200px; height: 1200px; overflow: hidden; background: var(--page); }
  .menu-board { position: absolute; left: 25px; top: 408px; width: 1151px; height: 288px; }
  .brick-frame {
    position: absolute; inset: 0;
    background: linear-gradient(180deg, var(--brick), #8c1a1f);
  }
  .menu-panel {
    position: absolute; left: 48px; top: 29px; width: 1062px; height: 226px;
    background: var(--panel); font-family: "Oswald", sans-serif; color: var(--ink);
  }
  .column { position: absolute; top: 12px; }
  .col-beef { left: 25px; width: 240px; }
  .col-chicken { left: 273px; width: 242px; }
  .col-sides { left: 690px; width: 310px; }
  .section-banner {
    height: 20px; background: var(--blue); color: #fff;
    font-weight: 600; font-size: 12px; letter-spacing: 1.5px; text-align: center; line-height: 20px;
    border-radius: 2px 10px 2px 10px;
  }
  .col-sides .section-banner { margin: 0 30px; }
  .section-intro {
    color: var(--blue); font-weight: 600; font-size: 7px; text-align: center;
    line-height: 1.2; margin: 7px 30px 3px;
  }
  .item-list { margin: 0 34px 0 37px; }
  .col-chicken .item-list { margin: 0 38px 0 26px; }
  .item { margin-top: 2px; }
  .item-head {
    display: flex; align-items: baseline; color: var(--blue); font-weight: 600; font-size: 7.5px; line-height: 1.15;
  }
  .item-head .dots { flex: 1; border-bottom: 1px dashed var(--blue); margin: 0 2px 2px; }
  .item-desc { font-size: 5.6px; line-height: 1.35; text-transform: uppercase; font-weight: 500; }
  .brand { position: absolute; left: 515px; top: 44px; width: 160px; text-align: center; }
  .brand-name {
    font-family: "Oswald", sans-serif; font-weight: 700; color: var(--blue);
    font-size: 36px; line-height: 1.05; text-transform: uppercase;
  }
  .brand-tag {
    font-family: "Josefin Sans", sans-serif; font-weight: 600; color: var(--blue);
    font-size: 7.5px; letter-spacing: 2px; margin-top: 42px; white-space: nowrap;
  }
  .sides-list { margin: 8px 45px 0 40px; }
  .sides-list .item-head { font-size: 8.5px; }
  .sub-rule {
    display: flex; align-items: center; gap: 6px; margin-top: 5px;
    color: var(--blue); font-weight: 600; font-size: 7px;
  }
  .sub-rule::before, .sub-rule::after { content: ""; flex: 1; height: 2px; background: var(--blue); }
  .steps { display: flex; gap: 0; margin: 4px 30px 0; }
  .step { flex: 1; padding: 0 3px; }
  .steps-band {
    display: flex; background: var(--blue); color: #fff; font-weight: 600; font-size: 7px;
    height: 12px; line-height: 12px; margin: 4px 30px 0;
  }
  .steps-band span { flex: 1; text-align: center; }
  .step-note { font-size: 5px; font-weight: 600; text-align: center; margin: 3px 0; }
  .step-line { font-size: 4.6px; line-height: 1.4; text-transform: uppercase; margin-bottom: 4px; }
  .ribs-title { color: var(--blue); font-weight: 600; font-size: 8px; text-align: center; margin-top: 1px; }
  .ribs-desc { font-size: 4.8px; text-align: center; text-transform: uppercase; line-height: 1.35; margin: 1px 50px; }
  .ribs-grid { display: flex; justify-content: center; gap: 36px; font-size: 4.8px; text-transform: uppercase; line-height: 1.4; margin-top: 3px; }
</style>
</head>
<body>
<div class="menu-board">
  <div class="brick-frame" role="img" aria-label="Red brick wall pattern border"></div>
  <div class="menu-panel">

    <section class="column col-beef">
      <h2 class="section-banner">BEEF BURGERS</h2>
      <p class="section-intro">ALL OUR PATTIES ARE 100% NATURAL BEEF WE KNOW BECAUSE WE GRIND IT OURSELVES SMASHED TO ORDER ON A HOT GRILL RITE IN FRONT OF YOU.</p>
      <div class="item-list">
        <div class="item"><div class="item-head">CLASSIC BEEF<span class="dots"></span>8.9</div>
          <p class="item-desc">Shredded lettuce, sliced tomato, caramelised onions, beetroot and BBQ sauce on a buttered sesame seed bun.</p></div>
        <div class="item"><div class="item-head">CHEESE BURGER<span class="dots"></span>9.5</div>
          <p class="item-desc">Dill pickles, minced onion, american cheese, mustard and ketchup on a soft milk bun.</p></div>
        <div class="item"><div class="item-head">FLAME GRILL<span class="dots"></span>9.5</div>
          <p class="item-desc">Shredded lettuce, sliced tomato, minced onions, dill pickles, american cheese, mayo and ketchup on a soft milk bun.</p></div>
        <div class="item"><div class="item-head">DOUBLE STACK<span class="dots"></span>9.5</div>
          <p class="item-desc">Shredded lettuce, dill pickles, minced onion, american cheese and house sauce on a soft milk bun.</p></div>
        <div class="item"><div class="item-head">TRUFFLED<span class="dots"></span>9.5</div>
          <p class="item-desc">Rocket, caramelised onion, dill pickles, havarti cheese and truffle infused mayo on a soft milk bun.</p></div>
      </div>
    </section>

    <section class="column col-chicken">
      <h2 class="section-banner">CHICKEN BURGERS</h2>
      <p class="section-intro">ALL OUR BURGER PATTIES ARE PREPARED<br>ONSITE DAILY USING PREMIUM<br>QUALITY CHICKEN BREAST</p>
      <div class="item-list">
        <div class="item"><div class="item-head">CLASSIC CHICKEN<span class="dots"></span>8.9</div>
          <p class="item-desc">Shredded lettuce, cheese and mayo on a classic sesame seed bun.</p></div>
        <div class="item"><div class="item-head">PIRRI PIRRI<span class="dots"></span>9.5</div>
          <p class="item-desc">Shredded lettuce, cheese, mayo and house made pirri pirri on a classic sesame seed bun.</p></div>
        <div class="item"><div class="item-head">KENTUCKY<span class="dots"></span>9.5</div>
          <p class="item-desc">Shredded lettuce, swiss cheese and zesty mayo on a soft milk bun.</p></div>
        <div class="item"><div class="item-head">EL BURGER<span class="dots"></span>9.5</div>
          <p class="item-desc">Shredded lettuce, salsa, guacamole, cheese, and chipotle mayo on a classic sesame seed bun.</p></div>
      </div>
    </section>

    <div class="brand">
      <div class="brand-name">Harbor<br>Burger</div>
      <p class="brand-tag">GRILLED FRESH EVERY DAY</p>
    </div>

    <section class="column col-sides">
      <h2 class="section-banner">SIDES</h2>
      <div class="sides-list">
        <div class="item-head">FRIES<span class="dots"></span>3.5</div>
        <div class="item-head">KENTUCKY TENDERS<span class="dots"></span>6.9</div>
      </div>
      <div class="sub-rule">NACHOS AND LOADED FRIES</div>
      <div class="steps-band"><span>STEP ONE</span><span>STEP TWO</span></div>
      <div class="steps">
        <div class="step">
          <p class="step-note">CHOOSE EITHER</p>
          <p class="step-line">Seasoned fries ------------ 6.9<br>or nacho chips</p>
          <p class="step-line">Curly fries ------------ 7.5</p>
        </div>
        <div class="step">
          <p class="step-note">CHOOSE ONE</p>
          <p class="step-line">Guacamole, salsa, sour cream,<br>jalapeños, cheese sauce</p>
          <p class="step-line">Beef chilli, salsa, sour cream,<br>cheese sauce and chives</p>
        </div>
      </div>
      <h3 class="ribs-title">BUFFALO CHICKEN RIBS</h3>
      <p class="ribs-desc">Buffalo style fried chicken ribs smothered in one of our mouth watering sauces served with a side of ranch sauce.</p>
      <div class="ribs-grid">
        <p>6 pack -------- 6.9<br>12 pack -------- 12.9<br>24 pack -------- 23.9</p>
        <p>Classic hot sauce<br>or smoky BBQ</p>
      </div>
    </section>

  </div>
</div>
</body>
</html>
```